Label and packaging design for a cosmetic oil brand

I would like you to design the label and inside (bottle) / outside (box) packaging of my cosmetic Argan Oil brand.

I hope you can design a high quality label and packaging that stands out from the competition, highlighting sustainability and the elegance of a cosmetic brand.

You will find in the Word document attached more details on the specifications and the text for the label. Also, you will find examples of packaging styles that I like.

Thank you.

```html
<!DOCTYPE html>
<html lang="en">
<head>
<meta charset="utf-8">
<title>Maison Sauge – Packaging System</title>
<link href="https://fonts.googleapis.com/css2?family=Lato:ital,wght@0,400;0,700;1,400&family=Montserrat:wght@300&display=swap" rel="stylesheet">
<style>
  :root{
    --stage:#b3bfb0;
    --title:#e9eee6;
    --cream:#e0d9c8;
    --olive:#6b7c4c;
    --olive-deep:#556339;
    --ink:#3d3a33;
    --gold:#c9a94f;
    --gold-soft:#e6d693;
  }
  *{margin:0;padding:0;box-sizing:border-box}
  html,body{width:1200px;height:916px;overflow:hidden;background:var(--stage)}
  body{position:relative;font-family:"Lato",sans-serif;color:var(--ink)}

  .section-title{position:absolute;font-family:"Montserrat",sans-serif;font-weight:300;font-size:30px;letter-spacing:2px;color:var(--title);text-align:center;line-height:1.2}
  .section-title--box{left:274px;top:38px;width:300px}
  .section-title--inside{left:840px;top:183px;width:300px}
  .section-title--bottle{left:271px;top:616px;width:300px}

  /* ---------- Box dieline ---------- */
  .box{position:absolute;left:66px;top:99px;width:718px;height:484px;background:var(--cream);box-shadow:2px 3px 6px rgba(0,0,0,.18);display:flex}
  .box-panel{position:relative;height:100%;overflow:hidden}
  .box-panel--back{width:198px;border-right:1px solid rgba(0,0,0,.08)}
  .box-panel--front{width:320px;border-right:1px solid rgba(0,0,0,.08)}
  .box-panel--side{width:200px}

  .rot{position:absolute;width:484px;height:198px;transform-origin:0 0}
  .rot--cw{left:198px;top:0;transform:rotate(90deg)}
  .rot--ccw{left:0;top:484px;width:484px;height:200px;transform:rotate(-90deg)}
  .rot p,.rot div{position:absolute}

  .copy{font-size:7.2px;line-height:10.2px;text-align:justify;color:var(--ink)}
  .copy b{color:var(--olive);font-weight:400}
  .copy--small{font-size:5.5px;line-height:7.4px}
  .copy--plain{text-align:left}
  .benefit-frame{border:1.5px solid var(--olive);padding:5px 8px}
  .benefit-title{display:block;text-align:center;font-size:7.2px;letter-spacing:1px;color:var(--olive);font-weight:700;margin-bottom:2px}

  .front{position:absolute;left:0;width:100%;text-align:center}
  .brand-name{font-weight:700;color:var(--gold)}
  .brand-tag{color:var(--gold-soft)}
  .brand-dot{position:absolute;left:50%;border-radius:50%;border:1.5px solid var(--gold)}
  .green-line{color:var(--olive)}
  .italic-line{font-style:italic;color:var(--ink)}
  .rule{position:absolute;left:50%;height:1.5px;background:var(--olive)}

  .badge{position:absolute;width:16px;height:16px;border-radius:50%;border:1px solid #6e6a60;background:var(--cream)}
  .mark{position:absolute}

  /* ---------- Inside label ---------- */
  .inside-card{position:absolute;left:828px;top:304px;width:320px;height:484px;background:var(--olive);box-shadow:2px 3px 6px rgba(0,0,0,.18);overflow:hidden}
  .inside-card .pattern{position:absolute;inset:0}
  .inside-card .bottle-art{position:absolute;left:134px;top:136px;width:76px;height:92px;border-radius:6px}
  .inside-url{position:absolute;top:262px;width:100%;text-align:center;font-size:10px;font-weight:700;color:var(--gold-soft)}
  .inside-tag{position:absolute;top:289px;width:100%;text-align:center;font-size:8.5px;line-height:13px;font-weight:700;color:var(--gold-soft)}
  .socials{position:absolute;top:342px;left:0;width:100%;display:flex;justify-content:center;gap:9px}
  .socials span{width:16px;height:16px;border-radius:50%;background:var(--gold-soft)}

  /* ---------- Bottle label ---------- */
  .bottle{position:absolute;left:210px;top:675px;width:416px;height:184px;background:var(--cream);box-shadow:2px 3px 6px rgba(0,0,0,.18);overflow:hidden}
  .bottle-band{position:absolute;left:0;top:0;width:100%;height:70px;background:var(--olive)}
  .bottle-band .pattern{position:absolute;inset:0}
  .bottle-gold{position:absolute;left:0;top:70px;width:100%;height:2px;background:var(--gold)}
  .bottle-brand{position:absolute;top:46px;width:100%;text-align:center;font-size:9px}
  .bottle-tag{position:absolute;top:58px;width:100%;text-align:center;font-size:4.6px}
  .bottle-col{position:absolute;top:81px;width:102px;font-size:5.4px;line-height:7.2px;text-align:justify}
  .bottle-col b{color:var(--olive);font-weight:400}
  .bottle-col--en{left:20px}
  .bottle-col--fr{left:294px;font-style:italic}
  .bottle-col p+p{margin-top:6px}
  .bottle-center{position:absolute;left:0;width:100%;text-align:center}
</style>
</head>
<body>

<h2 class="section-title section-title--box">Box Design</h2>
<h2 class="section-title section-title--inside">Box Label<br>Inside</h2>
<h2 class="section-title section-title--bottle">Bottle Label</h2>

<!-- Box dieline -->
<section class="box">
  <div class="box-panel box-panel--back">
    <div class="rot rot--cw">
      <p class="copy" style="left:21px;top:9px;width:210px"><b>Ingrédients:</b> Un seul ! Huile d'Argania Spinosa (Argan) 100% pure, pressée à froid et non parfumée, une riche source d'acides gras, d'antioxydants et de vitamine E.</p>
      <p class="copy" style="left:21px;top:44px;width:210px"><b>Mise en garde:</b> Pour usage externe uniquement, tenir hors des yeux. En cas de sensibilité cutanée, cesser l'utilisation.</p>
      <p class="copy" style="left:252px;top:9px;width:210px"><b>Mode d'emploi:</b> Appliquez sur vos cheveux et votre cuir chevelu pour nourrir, revitaliser et coiffer. Appliquez sur votre visage, votre peau et vos ongles pour hydrater et revitaliser. Utiliser quotidiennement pour de meilleurs résultats. Vous pouvez également l'utiliser comme huile de massage ou de bain.</p>
      <div class="benefit-frame copy copy--small" style="left:21px;top:72px;width:440px;height:66px">
        <span class="benefit-title">BIENFAITS</span>
        L'huile d'argan est considérée comme l'une des sources naturelles les plus riches en acides gras essentiels, en antioxydants et en vitamine E. Sa composition unique lui confère des propriétés revitalisantes et nourrissantes exceptionnelles qui favorisent une peau et des cheveux sains, éclatants et rajeunis. Par ailleurs, l'huile d'Argan Maison Sauge soutient des coopératives certifiées « Fair Trade », dirigées par des femmes dans des zones rurales sous-développées, contribuant à leur économie locale et assurant la bonne exploitation de l'Arganier protégé par l'UNESCO. En bref, elle vous permettra de prendre soin de votre santé et de votre beauté, tout en vous engageant pour le développement durable !
      </div>
      <p class="copy copy--plain" style="left:21px;top:148px;width:440px">Visitez <strong>maisonsauge.com</strong> pour plus d'informations et de détails sur l'huile d'Argan Maison Sauge,<br>ses bienfaits et comment l'utiliser.</p>
      <p class="copy copy--plain" style="left:21px;top:172px;width:440px">Importé du Maroc | Embouteillé et distribué par Maison Sauge<br>Lakeview, QC, Canada</p>
    </div>
    <svg class="mark" style="left:13px;top:420px" width="20" height="20" viewBox="0 0 20 20" aria-hidden="true"><circle cx="10" cy="10" r="8" fill="#2f2d29"/><path d="M6 10a4 4 0 0 1 7-2.6M14 10a4 4 0 0 1-7 2.6" stroke="#e0d9c8" stroke-width="1.6" fill="none"/></svg>
    <svg class="mark" style="left:13px;top:444px" width="20" height="18" viewBox="0 0 20 18" aria-hidden="true"><rect x="1" y="4" width="11" height="12" rx="1.5" fill="#2f2d29"/><rect x="10" y="2" width="9" height="14" rx="3" fill="none" stroke="#2f2d29" stroke-width="1.6"/></svg>
  </div>

  <div class="box-panel box-panel--front">
    <span class="brand-dot" style="top:88px;width:44px;height:44px;margin-left:-22px"></span>
    <p class="front brand-name" style="top:139px;font-size:17px">Maison Sauge</p>
    <p class="front brand-tag" style="top:161px;font-size:8.5px">Pure care, grown with respect for the land and its people</p>
    <p class="front green-line" style="top:212px;font-size:13px">100% Pure Cosmetic</p>
    <p class="front green-line" style="top:227px;font-size:13px"><span style="font-size:16px">Argan Oil</span> of Morocco</p>
    <p class="front italic-line" style="top:255px;font-size:11px;line-height:14px">Huile d'Argan cosmétique<br>du Maroc 100% pure</p>
    <span class="rule" style="top:306px;width:55px;margin-left:-27px"></span>
    <p class="front green-line" style="top:332px;font-size:13px">Natural Hair and Skin Care</p>
    <p class="front italic-line" style="top:356px;font-size:11px;line-height:14px">Soins naturels<br>de la peau et des cheveux</p>
    <p class="front green-line" style="top:417px;font-size:13px;font-weight:700">1 oz | 30 ml</p>
  </div>

  <div class="box-panel box-panel--side">
    <div class="rot rot--ccw">
      <p class="copy" style="left:22px;top:10px;width:212px"><b>Ingredients:</b> Only one ! 100% pure, cold-pressed and unscented Argania Spinosa (Argan) kernel Oil, a rich source of fatty acids, antioxidants, and vitamin E.</p>
      <p class="copy" style="left:22px;top:44px;width:212px"><b>Caution:</b> For external use only, keep out of the eyes. If skin sensitivity occurs, discontinue use.</p>
      <p class="copy" style="left:253px;top:10px;width:210px"><b>How to use:</b> Apply to your hair and scalp to nourish, condition and style. Apply to your face, skin and nails to hydrate, moisturize and condition. Use daily for better results. You can also use it as a massage or bath oil.</p>
      <div class="benefit-frame copy copy--small" style="left:22px;top:73px;width:441px;height:65px">
        <span class="benefit-title">BENEFITS</span>
        Argan Oil is considered one of nature's richest sources of essential fatty acids, antioxidants, and vitamin E. Its unique composition grants it amazing conditioning and nourishing properties that naturally promote healthy, radiant, youthful skin and hair. Besides, Maison Sauge Argan Oil supports Fair-Trade certified women-led cooperatives in underdeveloped rural areas, contributing to their local economy and ensuring the good exploitation of the UNESCO protected Argan tree. In an Argan nutshell, it will allow you to take care of your health and beauty, while standing for sustainability !
      </div>
      <p class="copy copy--plain" style="left:22px;top:150px;width:290px">Visit <strong>maisonsauge.com</strong> for more information and details on Maison Sauge Argan Oil,<br>its benefits and how to use it.</p>
      <p class="copy copy--plain" style="left:22px;top:172px;width:290px">Imported from Morocco | Bottled and Distributed by Maison Sauge<br>Lakeview, QC, Canada</p>
    </div>
    <span class="badge" style="left:169px;top:21px"></span>
    <span class="badge" style="left:169px;top:43px"></span>
    <span class="badge" style="left:169px;top:65px"></span>
    <span class="badge" style="left:169px;top:87px"></span>
    <span class="badge" style="left:169px;top:109px"></span>
    <span class="badge" style="left:169px;top:131px"></span>
    <span class="badge" style="left:169px;top:153px"></span>
  </div>
</section>

<!-- Inside box label -->
<section class="inside-card">
  <svg class="pattern" width="320" height="484" role="img" aria-label="Hand-drawn argan branches, leaves and nuts in deep olive line work framing the card">
    <defs><radialGradient id="leafShade" cx="50%" cy="50%" r="70%"><stop offset="55%" stop-color="#6b7c4c"/><stop offset="100%" stop-color="#617045"/></radialGradient></defs>
    <rect width="320" height="484" fill="url(#leafShade)"/>
  </svg>
  <svg class="bottle-art" viewBox="0 0 76 92" role="img" aria-label="Gold line sketch of a dropper bottle with argan fruit branch">
    <defs><linearGradient id="goldArt" x1="0" y1="0" x2="1" y2="1"><stop offset="0" stop-color="#d9c77f" stop-opacity=".55"/><stop offset="1" stop-color="#b9a45c" stop-opacity=".35"/></linearGradient></defs>
    <rect width="76" height="92" rx="6" fill="url(#goldArt)"/>
  </svg>
  <p class="inside-url">maisonsauge.com</p>
  <p class="inside-tag">Pure care, grown with respect<br>for the land and its people</p>
  <div class="socials"><span></span><span></span><span></span></div>
</section>

<!-- Bottle label -->
<section class="bottle">
  <div class="bottle-band">
    <svg class="pattern" width="416" height="70" role="img" aria-label="Hand-drawn argan leaves and nuts pattern in olive tones">
      <defs><linearGradient id="bandShade" x1="0" y1="0" x2="1" y2="0"><stop offset="0" stop-color="#657548"/><stop offset=".5" stop-color="#6b7c4c"/><stop offset="1" stop-color="#657548"/></linearGradient></defs>
      <rect width="416" height="70" fill="url(#bandShade)"/>
    </svg>
    <span class="brand-dot" style="top:10px;width:30px;height:30px;margin-left:-15px"></span>
    <p class="bottle-brand brand-name">Maison Sauge</p>
    <p class="bottle-tag brand-tag">Pure care, grown with respect for the land and its people</p>
  </div>
  <span class="bottle-gold"></span>

  <div class="bottle-col bottle-col--en">
    <p><b>Ingredients:</b> Only one ! 100% pure, cold-pressed and unscented Argania Spinosa (Argan) kernel Oil, a rich source of fatty acids, antioxidants, and vitamin E.</p>
    <p><b>Caution:</b> For external use only, keep out of the eyes. If skin sensitivity occurs, discontinue use.</p>
  </div>

  <p class="bottle-center green-line" style="top:82px;font-size:6.6px">100% Pure Cosmetic</p>
  <p class="bottle-center green-line" style="top:89px;font-size:8px">Argan Oil of Morocco</p>
  <p class="bottle-center italic-line" style="top:100px;font-size:6px;line-height:7.2px">Huile d'Argan cosmétique<br>du Maroc 100% pure</p>
  <span class="rule" style="top:122px;width:28px;margin-left:-14px;height:1px"></span>
  <p class="bottle-center green-line" style="top:130px;font-size:6.6px">Natural Hair and Skin Care</p>
  <p class="bottle-center italic-line" style="top:140px;font-size:5.8px;line-height:7.2px">Soins naturels<br>de la peau et des cheveux</p>
  <p class="bottle-center green-line" style="top:168px;font-size:5px">1 oz | 30 ml</p>

  <div class="bottle-col bottle-col--fr">
    <p><b>Ingrédients:</b> Un seul ! Huile d'Argania Spinosa (Argan) 100% pure, pressée à froid et non parfumée, une riche source d'acides gras, d'antioxydants et de vitamine E.</p>
    <p><b>Mise en garde:</b> Pour usage externe uniquement, tenir hors des yeux. En cas de sensibilité cutanée, cesser l'utilisation.</p>
  </div>

  <svg class="mark" style="left:370px;top:162px" width="11" height="11" viewBox="0 0 20 20" aria-hidden="true"><circle cx="10" cy="10" r="8" fill="#2f2d29"/><path d="M6 10a4 4 0 0 1 7-2.6M14 10a4 4 0 0 1-7 2.6" stroke="#e0d9c8" stroke-width="1.8" fill="none"/></svg>
  <svg class="mark" style="left:384px;top:161px" width="11" height="11" viewBox="0 0 20 18" aria-hidden="true"><rect x="1" y="4" width="11" height="12" rx="1.5" fill="#2f2d29"/><rect x="10" y="2" width="9" height="14" rx="3" fill="none" stroke="#2f2d29" stroke-width="1.8"/></svg>
</section>

</body>
</html>
```